Brivolands Vehicle Wrap Design for Vacation Rental Property Mgt Company

We are looking for a vehicle wrap design to extend our brand through our service vehicles. Design should be simple, professional, eye-catching, and incorporate our logo and corporate colors. Design should be flexible enough to be applied to a wide variety of trucks and cars. Not looking for FULL wrap, but rather separate graphics to be applied to white vehicles. Attached is ppt with a couple of our current vehicles and a few sample designs that has caught our attention. Copies of our current logo and biz card designs are also included.

Panels to include:
Logo (attached)
555-384-9126
www.Brivolands.example
Vacation Rental Property Management
Property Maintenance Services
Linen & Laundry Services

Target Market(s)

Local adults 30-65

Industry/Entity Type

Font styles to use
Serif

Colors
0054AA
0677BA
7BADD7
CADEEF
E8F1F8

Requirements
Must have
• Logo, phone, web address, corporate colors,

```html
<!DOCTYPE html>
<html lang="en">
<head>
<meta charset="utf-8">
<title>Brivolands Vehicle Wrap</title>
<link rel="stylesheet" href="https://fonts.googleapis.com/css2?family=Antonio:wght@600&family=Montserrat:wght@600&family=Open+Sans:wght@500&display=swap">
<style>
  :root {
    --navy: #1a305e;
    --sky: #2b8fc6;
    --sky-light: #3b9fd3;
    --white: #ffffff;
    --text-light: #e6e8ee;
  }
  html, body {
    margin: 0;
    padding: 0;
    width: 1200px;
    height: 900px;
    overflow: hidden;
    background: var(--white);
  }
  .wrap-panel {
    position: relative;
    width: 1200px;
    height: 900px;
  }
  .wrap-bands {
    position: absolute;
    inset: 0;
  }
  .brand {
    position: absolute;
    left: 470px;
    top: 262px;
    display: flex;
    align-items: center;
    gap: 26px;
  }
  .brand-mark {
    width: 92px;
    height: 92px;
    background: var(--navy);
  }
  .brand-name {
    font-family: "Antonio", sans-serif;
    font-weight: 600;
    font-size: 74px;
    line-height: 1;
    letter-spacing: 1px;
    color: var(--navy);
    text-transform: uppercase;
  }
  .brand-tagline {
    position: absolute;
    left: 650px;
    top: 344px;
    font-family: "Montserrat", sans-serif;
    font-weight: 600;
    font-size: 16px;
    letter-spacing: 1px;
    color: var(--navy);
  }
  .contact {
    position: absolute;
    right: 360px;
    top: 475px;
    text-align: right;
    font-family: "Open Sans", sans-serif;
    font-weight: 500;
    color: var(--text-light);
  }
  .contact-phone {
    font-size: 31px;
    line-height: 1.1;
  }
  .contact-web {
    font-size: 33px;
    line-height: 1.1;
  }
</style>
</head>
<body>
<main class="wrap-panel">
  <svg class="wrap-bands" width="1200" height="900" viewBox="0 0 1200 900" aria-hidden="true">
    <path class="band-navy-top" fill="var(--navy)" d="M0 455 C150 455 300 452 420 448 L420 452 C300 458 150 462 0 463 Z"/>
    <path class="band-sky" fill="var(--sky)" d="M0 480 C300 482 650 420 900 390 C1000 380 1100 382 1200 388 L1200 410 C1050 402 900 410 760 430 C560 458 300 492 0 492 Z"/>
    <path class="band-sky-inner" fill="var(--sky-light)" d="M620 440 C800 418 1000 410 1200 418 L1200 436 C1000 428 820 432 620 440 Z"/>
    <path class="band-navy" fill="var(--navy)" d="M0 500 C300 502 600 470 850 445 C980 434 1100 432 1200 434 L1200 640 L0 640 Z"/>
  </svg>

  <div class="brand">
    <div class="brand-mark"></div>
    <div class="brand-name">Brivolands</div>
  </div>
  <div class="brand-tagline">VACATION RENTALS</div>

  <div class="contact">
    <div class="contact-phone">555-384-9126</div>
    <div class="contact-web">www.Brivolands.example</div>
  </div>
</main>
</body>
</html>
```